Korvane Business Cards

We need a business card design. We are a Technology (Audio Visual) design, sales and installation company. Looking for a double sided design, clean

Contact Information for Business Card

Clean, modern look, 2 sided

Font styles to use
Sans Serif

```html
<!DOCTYPE html>
<html lang="en">
<head>
<meta charset="utf-8">
<title>Korvane Business Card</title>
<link rel="stylesheet" href="https://fonts.googleapis.com/css2?family=Montserrat:wght@500;600;700&family=Arimo&display=swap">
<style>
  :root {
    --backdrop: #97a7b1;
    --navy: #1d3242;
    --orange: #f69322;
    --white: #ffffff;
    --title-ink: #2b2b2b;
  }
  * { box-sizing: border-box; margin: 0; padding: 0; }
  html, body { width: 720px; height: 1200px; overflow: hidden; }
  body {
    background: var(--backdrop);
    font-family: "Montserrat", sans-serif;
    position: relative;
  }
  .sheet-title {
    position: absolute; left: 30px; top: 58px;
    font-family: "Arimo", sans-serif; font-size: 30px; font-weight: 400;
    color: var(--title-ink);
  }
  .card {
    position: absolute; left: 30px; width: 660px; height: 377px; overflow: hidden;
  }
  .card--front { top: 130px; background: var(--white); }
  .card--back { top: 537px; background: var(--navy); }

  .edge-block {
    position: absolute; left: 0; top: 43px; width: 37px; height: 69px;
    background: var(--navy);
  }
  .wordmark {
    position: absolute; font-weight: 700; line-height: 1; letter-spacing: -1px;
  }
  .card--front .wordmark {
    left: 62px; top: 55px; font-size: 48px; color: var(--navy);
  }
  .name-band {
    position: absolute; left: 300px; right: 0; top: 43px; height: 69px;
    background: var(--orange);
    padding-right: 53px; text-align: right;
    color: var(--navy);
  }
  .owner-name { font-size: 20px; font-weight: 700; margin-top: 12px; line-height: 1.1; }
  .designation { font-size: 16px; font-weight: 600; line-height: 1.2; }

  .contact-list { position: absolute; left: 72px; top: 144px; list-style: none; }
  .contact-item {
    display: flex; align-items: center; height: 38px; margin-bottom: 11px;
    color: var(--navy); font-size: 17px; font-weight: 500; line-height: 21px;
  }
  .contact-icon {
    width: 38px; height: 38px; flex: none; margin-right: 15px;
  }

  .card--back .wordmark {
    left: 0; right: 0; top: 132px; text-align: center;
    font-size: 72px; color: var(--white);
  }
  .back-url {
    position: absolute; left: 0; right: 0; top: 283px; text-align: center;
    color: var(--white); font-size: 24px; font-weight: 500;
  }
</style>
</head>
<body>
  <h1 class="sheet-title">Business Card: Dimensions&nbsp; 3.5" x 2.0"</h1>

  <section class="card card--front" aria-label="Card front">
    <div class="edge-block"></div>
    <div class="wordmark">Korvane</div>
    <div class="name-band">
      <p class="owner-name">Owner’s Name</p>
      <p class="designation">Designation</p>
    </div>
    <ul class="contact-list">
      <li class="contact-item">
        <svg class="contact-icon" viewBox="0 0 38 38" aria-hidden="true">
          <circle cx="19" cy="19" r="18" fill="none" stroke="#1d3242" stroke-width="1.3"/>
          <rect x="14" y="10" width="10" height="18" rx="1.5" fill="none" stroke="#1d3242" stroke-width="1.6"/>
          <circle cx="19" cy="25.5" r="0.9" fill="#1d3242"/>
        </svg>
        555-014-2270 - dummy no.
      </li>
      <li class="contact-item">
        <svg class="contact-icon" viewBox="0 0 38 38" aria-hidden="true">
          <circle cx="19" cy="19" r="18" fill="none" stroke="#1d3242" stroke-width="1.3"/>
          <rect x="11" y="14" width="16" height="11" rx="1" fill="#1d3242"/>
          <path d="M11.5 14.5 L19 20.5 L26.5 14.5 M11.5 24.5 L17 19.5 M26.5 24.5 L21 19.5" fill="none" stroke="#fff" stroke-width="1"/>
        </svg>
        info@korvane.com
      </li>
      <li class="contact-item">
        <svg class="contact-icon" viewBox="0 0 38 38" aria-hidden="true">
          <circle cx="19" cy="19" r="18" fill="none" stroke="#1d3242" stroke-width="1.3"/>
          <path d="M19 29 C15 23 13 20 13 16.5 A6 6 0 0 1 25 16.5 C25 20 23 23 19 29 Z" fill="#1d3242"/>
          <circle cx="19" cy="16.5" r="2.2" fill="#fff"/>
        </svg>
        <span>Company address and or<br>branch address</span>
      </li>
      <li class="contact-item">
        <svg class="contact-icon" viewBox="0 0 38 38" aria-hidden="true">
          <circle cx="19" cy="19" r="18" fill="none" stroke="#1d3242" stroke-width="1.3"/>
          <circle cx="19" cy="19" r="8.5" fill="#1d3242"/>
          <path d="M10.5 19 H27.5 M19 10.5 V27.5 M12 14.5 H26 M12 23.5 H26" stroke="#fff" stroke-width="0.9"/>
          <ellipse cx="19" cy="19" rx="3.8" ry="8.5" fill="none" stroke="#fff" stroke-width="0.9"/>
        </svg>
        www.korvane.com
      </li>
    </ul>
  </section>

  <section class="card card--back" aria-label="Card back">
    <div class="wordmark">Korvane</div>
    <p class="back-url">www.korvane.com</p>
  </section>
</body>
</html>
```